Website design for Cambridge based systematic hedge fund

We have run previous craftmosaic competitions to design our company logo, business cards and the styling of our presentation deck (see attached files).
As the final step we are looking to get a website designed that is thematically consistent with these existing elements of our branding.
You can find some of our competitors websites below:
https://www.quelmarsh.example/
https://www.fenloor.example/
https://www.pyvart.example/
https://www.dulvet.example/
https://www.orbelmfunds.example/
https://www.valtrigo.example/
https://www.meskilfunds.example/home
We would like to have a website that works well on both mobile devices and desktops. Either just as one page that can be scrolled down, with links at the top that skips to certain sections, or a few separate pages that can be navigated by a top menu.
It should look professional, we are not after lots of animations or unnecessary transitions, and in particular the website must be smooth to navigate. We would like to avoid having peoples of people, we are happy to make use of elements from the presentation (for example the style of the cover slide, or the section slides with the faded bridge in the background), or 'financial' style images.
We would like to have the following sections for now. For some of these some example text has been provided, final text may change but it will be of similar length. For the other sections we are happy to just have template text for now. At the moment we are mainly interested to see styles/layouts as words can be added easily afterwards:
1) We will need a disclaimer pop up the first time someone visits the site (see for example the meskilfunds example).
2) Top page - company name, then in larger text "Bringing AI and Statistical Inference to Financial Markets", and somewhere in smaller text "Harlow Vectors is a quantitative asset manager with the singular focus of delivering algorithmic strategies that work"
3) "About us" section: will describe us as a company, details our approach, company values, and explains the company logo.
Example text:
"We deliver consistent alpha across liquid markets through the application of proprietary IP in Bayesian inference, machine learning and artificial intelligence. We are a multi-disciplinary team founded by experienced finance professionals from premier institutions, leading academics from the Thornbury Stellar Unit at Ashmere College and world-class software engineers.
Our logo portrays a sillhoute of the lattice walkway at Ashmere College. Our unique scientific approach allows us to bridge cutting-edge mathematical research and computing expertise with financial knowledge to bring algorithmns that work to liquid markets"
4) Hiring section, detailing our culture, what we are looking for.
Example text:
"We are always looking for exceptional talent to join our entrepreneurial team. We are looking for individuals who are creative thinkers, can demonstrate analytical rigour and are passionate about the intersection of science, finance and technology.
We prioritise having a company culture that promotes sharing ideas in a safe, collaborative research environment. We make sure that every member of the team has the oppertunity to explore their own ideas through weekly 'innovation time', and ensure that everyone gets the support they need to continue to grow as individuals within the company."
5) A section for news/press releases
6) Contact us area at the bottom with office location and email. We will need to list 3 addresses for our Cambridge, London and Singapore offices, along with a couple of contact emails or phone numbers
7) A client login button at the top that will take them to a different website (unrelated to this one).

```html
<!DOCTYPE html>
<html lang="en">
<head>
<meta charset="utf-8">
<title>Harlow Vectors</title>
<link rel="stylesheet" href="https://fonts.googleapis.com/css2?family=Montserrat:wght@500;600;700;800&family=Lato:wght@400;700&display=swap">
<style>
:root{
  --navy:#0b4377;
  --navy-deep:#094273;
  --blue:#4f90d8;
  --blue-btn:#5b98db;
  --link:#2a8fd8;
  --ink:#222;
  --body:#444;
  --muted:#666;
  --pale:#f5f9fd;
  --rose:#9b5e78;
  --white:#fff;
}
*{box-sizing:border-box;margin:0;padding:0}
html,body{width:1200px;height:3145px;overflow:hidden}
body{font-family:"Lato",sans-serif;color:var(--body);background:var(--white);position:relative}
.wrap{width:918px;margin:0 auto;position:relative}
h1,h2,h3,h4,.nav a,.btn{font-family:"Montserrat",sans-serif}
.btn{display:inline-block;background:var(--blue-btn);color:var(--white);font-weight:700;font-size:14px;text-decoration:none;padding:13px 20px;border-radius:3px;letter-spacing:.2px}

/* header */
.site-header{height:112px}
.site-header .wrap{display:flex;align-items:center;height:112px}
.brand{display:flex;align-items:center;gap:10px;color:var(--navy);font-family:"Montserrat",sans-serif;font-weight:700;font-size:22px;text-decoration:none}
.brand-mark{width:14px;height:14px;background:var(--navy)}
.nav{margin-left:auto;display:flex;align-items:center;gap:31px}
.nav a{font-weight:600;font-size:14px;color:var(--ink);text-decoration:none}
.nav a.active{color:var(--link)}
.nav .btn{margin-left:0;padding:13px 31px;font-size:14px}

/* hero */
.hero{height:501px;background:radial-gradient(ellipse at 30% 20%,#2f72b6 0%,#145596 45%,#0a3f78 100%);color:var(--white);text-align:center;padding-top:143px}
.hero h1{font-size:35px;font-weight:700;line-height:45px;letter-spacing:.3px}
.hero p{font-family:"Montserrat",sans-serif;font-weight:500;font-size:23px;line-height:33px;margin-top:12px}
.hero .btn{margin-top:20px;padding:13px 20px}

/* about */
.about{height:415px;text-align:center;padding-top:78px}
.about h2{font-size:35px;font-weight:700;color:var(--navy);line-height:38px}
.about h2 span{display:block;font-size:25px;color:var(--blue);letter-spacing:3px;line-height:36px}
.about p{font-size:15.5px;line-height:26.5px;color:var(--body);margin:14px auto 0;width:818px}
.about .btn{margin-top:24px}

/* pillars */
.pillars{height:588px;position:relative}
.pillars-photo{position:absolute;inset:0;background:linear-gradient(100deg,#b9a89a 0%,#d9d5d0 30%,#eeeeed 55%,#e3ded8 100%)}
.pillars-card{position:absolute;left:570px;top:83px;width:488px;height:529px;background:var(--white);box-shadow:0 4px 18px rgba(0,0,0,.08);padding:44px 28px 0 36px}
.pillar{display:flex;gap:26px;height:158px}
.pillar svg{flex:none}
.pillar h3{font-size:17px;font-weight:600;color:var(--ink);margin-top:14px}
.pillar p{font-size:12px;line-height:19px;color:var(--body);margin-top:3px}

/* hiring */
.hiring{height:447px;text-align:center;padding-top:100px}
.hiring h2{font-size:35px;font-weight:700;color:var(--navy)}
.hiring h2 span{color:var(--blue)}
.hiring p{font-size:15.5px;line-height:26.5px;width:918px;margin:6px auto 0}
.hiring p + p{margin-top:9px}
.hiring .btn{margin-top:27px;padding:13px 31px}

/* news */
.news{height:700px;background:var(--pale);padding-top:78px}
.news h2{font-size:35px;font-weight:700;color:var(--navy);text-align:center}
.news h2 span{color:var(--blue)}
.news-grid{display:flex;justify-content:space-between;margin-top:22px}
.news-feature{width:375px;height:446px;background:var(--white);padding:58px 46px 0;position:relative}
.kicker{font-family:"Montserrat",sans-serif;font-weight:700;font-size:13px;letter-spacing:3px;color:var(--blue)}
.news-feature h3{font-size:26px;line-height:37px;font-weight:700;color:var(--navy);margin-top:24px}
.news-feature p{font-size:12.5px;line-height:19px;margin-top:30px;color:var(--body)}
.byline{display:flex;align-items:center;font-size:11px;color:var(--navy);font-weight:700;margin-top:31px}
.avatar{width:31px;height:31px;border-radius:50%;background:linear-gradient(#9aa3ad,#4d5560);margin-right:10px;flex:none}
.byline time{margin-left:auto;color:var(--blue);font-weight:400;font-size:10.5px}
.arrow-btn{width:46px;height:46px;border-radius:50%;background:var(--blue-btn);display:flex;align-items:center;justify-content:center}
.news-feature .arrow-btn{position:absolute;left:154px;bottom:-22px;width:68px;height:68px}
.news-list{width:477px}
.news-item{height:255px;padding-top:11px;position:relative;border-bottom:1px solid #e2e8ef}
.news-item + .news-item{border-bottom:none;padding-top:35px}
.news-item h3{font-size:19px;line-height:27px;font-weight:700;color:var(--navy);margin-top:14px;width:400px}
.news-item p{font-size:12px;line-height:19px;margin-top:9px;width:400px}
.news-item .byline{margin-top:21px;width:396px}
.news-item .arrow-btn{position:absolute;right:0;top:100px}
.news-item + .news-item .arrow-btn{top:124px}

/* footer */
.site-footer{height:338px;background:var(--navy-deep);color:var(--white);padding-top:89px}
.footer-cols{display:flex}
.site-footer h4{font-size:17px;font-weight:700;letter-spacing:.2px}
.site-footer h4::after{content:"";display:block;width:28px;height:2px;background:var(--blue);margin-top:8px}
.quick{width:190px}
.quick ul{list-style:none;margin-top:18px}
.quick li{font-size:13px;line-height:27px}
.quick li::before{content:"• "}
.offices{display:flex;margin-top:18px}
.office{width:253px;font-size:13px}
.office .row{display:flex;gap:10px;align-items:flex-start;margin-bottom:12px}
.office .row svg{flex:none;margin-top:1px}
.office strong{display:block;font-size:14.5px}
.office .line{line-height:18px}
.office .phone{font-size:15px}
.bottom-bar{height:44px;background:var(--blue-btn);color:var(--white);font-size:12.5px}
.bottom-bar .wrap{display:flex;align-items:center;height:44px}
.social{margin-left:auto;display:flex;gap:8px}
.social span{width:29px;height:29px;border:1.5px solid var(--white);border-radius:50%}
</style>
</head>
<body>

<header class="site-header">
  <div class="wrap">
    <a class="brand" href="#"><span class="brand-mark"></span>HARLOW VECTORS</a>
    <nav class="nav">
      <a class="active" href="#">HOME</a>
      <a href="#">ABOUT US</a>
      <a href="#">HIRING</a>
      <a href="#">NEWS</a>
      <a href="#">CONTACT US</a>
      <a class="btn" href="#">&#128100;&#xFE0E; LOGIN</a>
    </nav>
  </div>
</header>

<section class="hero" role="img" aria-label="Deep blue background with a glowing network of connected data points">
  <h1>BRINGING AI AND STATISTICAL<br>INFERENCE TO FINANCIAL MARKETS</h1>
  <p>Harlow Vectors Is A Quantitative Asset Manager With The<br>Singular Focus Of Delivering Algorithmic Strategies That Work</p>
  <a class="btn" href="#">CONTACT US TODAY</a>
</section>

<section class="about">
  <h2>ABOUT HARLOW<span>VECTORS</span></h2>
  <p>We deliver consistent alpha across liquid markets through the application of proprietary IP in Bayesian inference, machine learning and artificial intelligence. We are a multi-disciplinary team founded by experienced finance professionals from premier institutions, leading academics from the Thornbury Stellar Unit at Ashmere College and world-class software engineers.</p>
  <a class="btn" href="#">CONTACT US TODAY</a>
</section>

<section class="pillars">
  <div class="pillars-photo" role="img" aria-label="Softly faded photo of an office desk with a laptop, papers and a coffee mug"></div>
  <div class="pillars-card">
    <div class="pillar">
      <svg width="110" height="128" viewBox="0 0 110 128"><polygon points="55,4 104,32 104,96 55,124 6,96 6,32" fill="#fff" stroke="#e4e8ee" stroke-width="6"/><polygon points="55,12 97,36 97,92 55,116 13,92 13,36" fill="#0b4377"/><g fill="none" stroke="#fff" stroke-width="2.5"><circle cx="55" cy="50" r="8"/><circle cx="40" cy="66" r="6"/><circle cx="70" cy="66" r="6"/><path d="M30 88v-6a10 10 0 0 1 20 0v6M60 88v-6a10 10 0 0 1 20 0v6"/></g></svg>
      <div><h3>OUR APPROACH</h3><p>Lorem ipsum dolor sit amet, consectetur adipiscing elit, sed diam nonummy nibh euismod tincidunt ut laoreet dolore magna aliquam erat volutpat. Ut wisi enim ad minim veniam quis.</p></div>
    </div>
    <div class="pillar">
      <svg width="110" height="128" viewBox="0 0 110 128"><polygon points="55,4 104,32 104,96 55,124 6,96 6,32" fill="#fff" stroke="#e4e8ee" stroke-width="6"/><polygon points="55,12 97,36 97,92 55,116 13,92 13,36" fill="#5b98db"/><g fill="none" stroke="#fff" stroke-width="2.5" stroke-linejoin="round"><path d="M28 60l12-10 12 6 10-6 20 10-14 16-12 4-14-8z"/><path d="M48 66l8 6M54 62l8 6M60 58l8 6"/></g></svg>
      <div><h3>OUR VALUES</h3><p>Lorem ipsum dolor sit amet, consectetur adipiscing elit, sed diam nonummy nibh euismod tincidunt ut laoreet dolore magna aliquam erat volutpat. Ut wisi enim ad minim veniam quis.</p></div>
    </div>
    <div class="pillar">
      <svg width="110" height="128" viewBox="0 0 110 128"><polygon points="55,4 104,32 104,96 55,124 6,96 6,32" fill="#fff" stroke="#e4e8ee" stroke-width="6"/><polygon points="55,12 97,36 97,92 55,116 13,92 13,36" fill="#9b5e78"/><g fill="none" stroke="#fff" stroke-width="2.5"><circle cx="45" cy="54" r="9"/><circle cx="66" cy="54" r="9"/><path d="M28 82a17 14 0 0 1 34 0zM58 70a17 14 0 0 1 24 12H64"/></g></svg>
      <div><h3>OUR COMPANY</h3><p>Our unique scientific approach allows us to bridge cutting-edge mathematical research &amp; computing expertise with financial knowledge to bring algorithmns that work to liquid markets.</p></div>
    </div>
  </div>
</section>

<section class="hiring">
  <h2>WE ARE <span>HIRING</span></h2>
  <p>We are always looking for exceptional talent to join our entrepreneurial team. We are looking for individuals who are creative thinkers, can demonstrate analytical rigour and are passionate about the intersection of science, finance and technology.</p>
  <p>We prioritise having a company culture that promotes sharing ideas in a safe, collaborative research environment. We make sure that every member of the team has the oppertunity to explore their own ideas through weekly 'innovation time', and ensure that everyone gets the support they need to continue to grow as individuals within the company.</p>
  <a class="btn" href="#">JOIN OUR TEAM</a>
</section>

<section class="news">
  <h2>LATEST <span>NEWS</span></h2>
  <div class="wrap news-grid">
    <article class="news-feature">
      <div class="kicker">NEWS</div>
      <h3>Ut Wisi Enim Minnim Veniam Quis Nostrud Exerci Tatio Uller.</h3>
      <p>Lorem ipsum dolor sit amet, consecte adipiscing elit, sed diam nonummy nibh euismod tincidunt ut laoreet dolore magna aliquam.</p>
      <div class="byline"><span class="avatar"></span>by Elin R.<time>29 Aug 2021</time></div>
      <a class="arrow-btn" href="#"><svg width="26" height="18" viewBox="0 0 26 18"><path d="M1 9h23M16 1l8 8-8 8" fill="none" stroke="#fff" stroke-width="2"/></svg></a>
    </article>
    <div class="news-list">
      <article class="news-item">
        <div class="kicker">NEWS</div>
        <h3>Ut Wisi Enim Minnim Veniais Nostrud Exerci Tatio Uller.</h3>
        <p>Lorem ipsum dolor sit amet, consecte aing elit, sed diam nonummy nibh euismod tincidunt ut laoreet dolore magna aliquam.</p>
        <div class="byline"><span class="avatar"></span>by Elin R.<time>29 Aug 2021</time></div>
        <a class="arrow-btn" href="#"><svg width="18" height="14" viewBox="0 0 18 14"><path d="M1 7h15M10 1l6 6-6 6" fill="none" stroke="#fff" stroke-width="1.6"/></svg></a>
      </article>
      <article class="news-item">
        <div class="kicker">NEWS</div>
        <h3>Ut Wisi Enim Minnim Veniais Nostrud Exerci Tatio Uller.</h3>
        <p>Lorem ipsum dolor sit amet, consecte aing elit, sed diam nonummy nibh euismod tincidunt ut laoreet dolore magna aliquam.</p>
        <div class="byline"><span class="avatar"></span>by Elin R.<time>29 Aug 2021</time></div>
        <a class="arrow-btn" href="#"><svg width="18" height="14" viewBox="0 0 18 14"><path d="M1 7h15M10 1l6 6-6 6" fill="none" stroke="#fff" stroke-width="1.6"/></svg></a>
      </article>
    </div>
  </div>
</section>

<footer class="site-footer">
  <div class="wrap footer-cols">
    <div class="quick">
      <h4>QUICK LINKS</h4>
      <ul><li>Home</li><li>About Us</li><li>Hiring</li><li>News</li><li>Contact Us</li></ul>
    </div>
    <div>
      <h4>CONTACT DETAILS</h4>
      <div class="offices">
        <div class="office">
          <div class="row"><svg width="16" height="20" viewBox="0 0 16 20"><path d="M8 19s7-7 7-11A7 7 0 0 0 1 8c0 4 7 11 7 11z" fill="none" stroke="#fff" stroke-width="1.3"/><circle cx="8" cy="8" r="2.5" fill="none" stroke="#fff" stroke-width="1.3"/></svg><div class="line"><strong>Cambridge</strong>123 Lorem ipsum dolor sit amet, consectetuer adipiscing.</div></div>
          <div class="row"><svg width="16" height="14" viewBox="0 0 16 14"><rect x="1" y="1" width="14" height="12" fill="none" stroke="#fff" stroke-width="1.3"/><path d="M1 1l7 6 7-6" fill="none" stroke="#fff" stroke-width="1.3"/></svg>info@harlowvectors.example</div>
          <div class="row phone"><svg width="16" height="16" viewBox="0 0 16 16"><path d="M3 1l3 3-2 2a10 10 0 0 0 6 6l2-2 3 3-2 2C7 15 1 9 1 3z" fill="none" stroke="#fff" stroke-width="1.3"/></svg>123-456-7890</div>
        </div>
        <div class="office">
          <div class="row"><svg width="16" height="20" viewBox="0 0 16 20"><path d="M8 19s7-7 7-11A7 7 0 0 0 1 8c0 4 7 11 7 11z" fill="none" stroke="#fff" stroke-width="1.3"/><circle cx="8" cy="8" r="2.5" fill="none" stroke="#fff" stroke-width="1.3"/></svg><div class="line"><strong>London</strong>123 Lorem ipsum dolor sit amet, consectetuer adipiscing.</div></div>
          <div class="row"><svg width="16" height="14" viewBox="0 0 16 14"><rect x="1" y="1" width="14" height="12" fill="none" stroke="#fff" stroke-width="1.3"/><path d="M1 1l7 6 7-6" fill="none" stroke="#fff" stroke-width="1.3"/></svg>info@harlowvectors.example</div>
          <div class="row phone"><svg width="16" height="16" viewBox="0 0 16 16"><path d="M3 1l3 3-2 2a10 10 0 0 0 6 6l2-2 3 3-2 2C7 15 1 9 1 3z" fill="none" stroke="#fff" stroke-width="1.3"/></svg>123-456-7890</div>
        </div>
        <div class="office">
          <div class="row"><svg width="16" height="20" viewBox="0 0 16 20"><path d="M8 19s7-7 7-11A7 7 0 0 0 1 8c0 4 7 11 7 11z" fill="none" stroke="#fff" stroke-width="1.3"/><circle cx="8" cy="8" r="2.5" fill="none" stroke="#fff" stroke-width="1.3"/></svg><div class="line"><strong>Singapore</strong>123 Lorem ipsum dolor sit amet, consectetuer adipiscing.</div></div>
          <div class="row"><svg width="16" height="14" viewBox="0 0 16 14"><rect x="1" y="1" width="14" height="12" fill="none" stroke="#fff" stroke-width="1.3"/><path d="M1 1l7 6 7-6" fill="none" stroke="#fff" stroke-width="1.3"/></svg>info@harlowvectors.example</div>
          <div class="row phone"><svg width="16" height="16" viewBox="0 0 16 16"><path d="M3 1l3 3-2 2a10 10 0 0 0 6 6l2-2 3 3-2 2C7 15 1 9 1 3z" fill="none" stroke="#fff" stroke-width="1.3"/></svg>123-456-7890</div>
        </div>
      </div>
    </div>
  </div>
</footer>

<div class="bottom-bar">
  <div class="wrap">
    <span>Copyright © 2021 <strong>Harlow Vectors.</strong> All Rights Reserved.</span>
    <div class="social" aria-label="Social links"><span></span><span></span><span></span></div>
  </div>
</div>

</body>
</html>
```